Startup Drone Platform Company business card

We are needing a business card design for our employees. We are a startup drone platform. We are looking for a business card that has our logo on one side, with the employee/company details on the opposite side. We are looking for something that is very eye catching, modern, and bold.

Target Market(s)

This will target both drone pilots and drone businesses, along with all the industries that could utilize drone services (aerial video, aerial photos, inspections, 3d mapping, etc).

Industry/Entity Type

Business

```html
<!DOCTYPE html>
<html lang="en">
<head>
<meta charset="utf-8">
<title>Skyward Lift – Business Card</title>
<link rel="stylesheet" href="https://fonts.googleapis.com/css2?family=Open+Sans:wght@400;600&display=swap">
<style>
  :root {
    --backdrop: #3a3330;
    --card: #0d0d0e;
    --card-edge: #1b1b1c;
    --teal: #2bb3c0;
    --white: #f2f2f2;
    --silver: #b9bcc0;
    --divider: #232325;
  }
  * { margin: 0; padding: 0; box-sizing: border-box; }
  html, body {
    width: 1200px; height: 900px; overflow: hidden;
    background: var(--backdrop);
    font-family: "Open Sans", sans-serif;
  }
  .stage {
    position: relative; width: 1200px; height: 900px;
    display: flex; align-items: center; justify-content: center; gap: 60px;
  }
  .card {
    position: relative; width: 525px; height: 300px;
    background: var(--card);
    border: 1px solid var(--card-edge);
    box-shadow: 0 18px 40px rgba(0,0,0,0.45);
    overflow: hidden;
  }
  /* Details side */
  .card-details { display: flex; }
  .brand-panel {
    width: 230px; height: 100%;
    display: flex; align-items: center; justify-content: center;
    border-right: 1px solid var(--divider);
  }
  .brand {
    display: flex; align-items: center; gap: 10px;
    font-weight: 600; font-size: 21px; letter-spacing: 4px;
    text-transform: uppercase; color: var(--white);
  }
  .brand-dot { width: 12px; height: 12px; border-radius: 50%; background: var(--teal); }
  .info { padding: 70px 0 0 34px; color: var(--white); }
  .person-name { font-size: 22px; font-weight: 400; color: var(--teal); line-height: 1.1; }
  .person-role { font-size: 13px; margin-top: 3px; }
  .address { font-size: 13px; line-height: 1.35; margin-top: 16px; }
  .contacts { list-style: none; margin-top: 14px; font-size: 13px; line-height: 1.5; }
  .contacts li { display: flex; align-items: center; gap: 10px; }
  .contacts svg { width: 12px; height: 12px; flex: none; }
  /* Brand side */
  .card-brand { display: flex; align-items: center; justify-content: center; }
  .card-brand .brand { color: var(--silver); font-size: 24px; }
  .card-brand .brand-dot { background: var(--silver); }
</style>
</head>
<body>
<main class="stage">
  <section class="card card-details">
    <div class="brand-panel">
      <div class="brand"><span class="brand-dot"></span>Skyward Lift</div>
    </div>
    <div class="info">
      <p class="person-name">Marcus Hale</p>
      <p class="person-role">Managing Director</p>
      <p class="address">12345, Address Goes Here<br>Country Name, 123456.</p>
      <ul class="contacts">
        <li>
          <svg viewBox="0 0 24 24" aria-hidden="true"><path fill="#2bb3c0" d="M6.6 10.8a15 15 0 0 0 6.6 6.6l2.2-2.2a1 1 0 0 1 1-.25 11.4 11.4 0 0 0 3.6.57 1 1 0 0 1 1 1V20a1 1 0 0 1-1 1A17 17 0 0 1 3 4a1 1 0 0 1 1-1h3.5a1 1 0 0 1 1 1c0 1.25.2 2.45.57 3.57a1 1 0 0 1-.25 1z"/></svg>
          044-555 210 384
        </li>
        <li>
          <svg viewBox="0 0 24 24" aria-hidden="true"><rect x="2" y="5" width="20" height="14" fill="#2bb3c0"/><path d="M2 5l10 8 10-8" fill="none" stroke="#0d0d0e" stroke-width="2"/></svg>
          info@skywardlift.com
        </li>
        <li>
          <svg viewBox="0 0 24 24" aria-hidden="true"><g fill="none" stroke="#2bb3c0" stroke-width="3" stroke-linecap="round"><path d="M10 14l4-4"/><path d="M8 12l-3 3a3.5 3.5 0 0 0 5 5l3-3"/><path d="M16 12l3-3a3.5 3.5 0 0 0-5-5l-3 3"/></g></svg>
          www.skywardlift.com
        </li>
      </ul>
    </div>
  </section>

  <section class="card card-brand">
    <div class="brand"><span class="brand-dot"></span>Skyward Lift</div>
  </section>
</main>
</body>
</html>
```